Local Roofing/Construction company business needs new biz card design

We need a new business card design, current cards are from the start of this operation and generic at best. We are a local Construction Company (General Contractor) with a majority of our work originating from insurance claims-exterior finish work is the main focus (Roofs-Siding-Gutters etc). Heavily involved with homeowners and the low ball offers they receive from insurance company's after a insurable event takes place. I have attached some of our original logo file(s) below.

```html
<!DOCTYPE html>
<html lang="en">
<head>
<meta charset="utf-8">
<title>Tallow Crest Construction – Business Card</title>
<link rel="stylesheet" href="https://fonts.googleapis.com/css2?family=Exo+2:wght@400;500;700;800&display=swap">
<style>
  :root {
    --bg: #2b2b2b;
    --green: #22d97a;
    --ink: #0f1e22;
    --paper: #ffffff;
    --muted: #e6ecec;
    --title: #1a2a2e;
  }
  * { margin: 0; padding: 0; box-sizing: border-box; }
  html, body { width: 1200px; height: 900px; overflow: hidden; }
  body {
    background: var(--bg);
    font-family: "Exo 2", sans-serif;
    position: relative;
  }
  .card {
    position: absolute;
    left: 300px;
    width: 600px;
    height: 343px;
    overflow: hidden;
    box-shadow: 0 8px 24px rgba(0,0,0,.45);
  }
  .card-front { top: 92px; background: var(--green); }
  .card-back  { top: 465px; background: var(--ink); }

  /* front */
  .front-brand {
    position: absolute;
    left: 50%; top: 50%;
    transform: translate(-50%, -50%);
    display: flex; align-items: center; gap: 14px;
    color: var(--ink);
    font-weight: 800;
    font-size: 27px;
    letter-spacing: .5px;
    white-space: nowrap;
  }
  .brand-square { width: 30px; height: 30px; background: var(--ink); flex: none; }

  /* back */
  .name-band {
    position: absolute; left: 0; top: 0;
    width: 100%; height: 132px;
    background: var(--paper);
  }
  .person { position: absolute; left: 56px; top: 76px; }
  .person-name {
    color: var(--green);
    font-weight: 700;
    font-size: 19px;
    letter-spacing: 1px;
    text-transform: uppercase;
  }
  .person-title {
    color: var(--title);
    font-weight: 500;
    font-size: 13.5px;
    letter-spacing: .6px;
    text-transform: uppercase;
    margin-top: 2px;
  }
  .back-brand {
    position: absolute; right: 46px; top: 36px;
    display: flex; flex-direction: column; align-items: center; gap: 8px;
  }
  .back-brand .brand-square { width: 120px; height: 110px; background: var(--green); border-radius: 10px; }
  .back-brand-name {
    color: var(--green);
    font-weight: 700;
    font-size: 11px;
    letter-spacing: .6px;
    text-align: center;
    line-height: 1.2;
  }
  .contact {
    position: absolute; left: 56px; top: 196px;
    color: var(--muted);
    font-size: 15px;
    line-height: 21px;
  }
  .contact-line { display: flex; align-items: center; gap: 8px; }
  .contact-line svg { width: 13px; height: 13px; fill: var(--green); flex: none; }
  .address { margin-top: 12px; }
  .website { margin-top: 12px; color: var(--green); }
</style>
</head>
<body>
  <section class="card card-front" aria-label="Card front">
    <div class="front-brand">
      <span class="brand-square"></span>
      <span>TALLOW CREST CONSTRUCTION</span>
    </div>
  </section>

  <section class="card card-back" aria-label="Card back">
    <div class="name-band"></div>
    <div class="person">
      <div class="person-name">Daniel Marlowe</div>
      <div class="person-title">Managing Director</div>
    </div>
    <div class="back-brand">
      <span class="brand-square"></span>
      <span class="back-brand-name">TALLOW CREST<br>CONSTRUCTION</span>
    </div>
    <div class="contact">
      <div class="contact-line">
        <svg viewBox="0 0 16 16" aria-hidden="true"><path d="M3 2h3l1.5 3.5-2 1.3a8 8 0 0 0 3.7 3.7l1.3-2L14 10v3a1 1 0 0 1-1 1A12 12 0 0 1 2 3a1 1 0 0 1 1-1z"/></svg>
        <span>555-214-0387</span>
      </div>
      <div class="contact-line">
        <svg viewBox="0 0 16 16" aria-hidden="true"><path d="M1 3h14v10H1z M1 3l7 6 7-6" stroke="#0f1e22" stroke-width="1.2"/></svg>
        <span>info@tallowcrestbuild.com</span>
      </div>
      <div class="address">48 Orchard Valley Rd<br>Fairbrook, MO 63010</div>
      <div class="website">www.tallowcrestbuild.com</div>
    </div>
  </section>
</body>
</html>
```